Computer consultant business card

Brimlo Software is a newly started computer consulting company. It's a small one-man company that provides mostly Velunix applications but also websites in collaboration with designers. I'm running this company on the side of full time university studies.

I want the final design to be clean and memorable. Be creative! :)

Some inspiration:
http://www.tavelpix.net/design/73519
http://www.tavelpix.net/design/2739566/business-card-design-by-quillbop
http://www.tavelpix.net/design/804613/business-card-design-by-lorvena-brukwaldsen

See attachment for my company logo.
Updates

I would like to thank everyone for submitting! I'll need a couple of days to review and ultimately select a design.

Target Market(s)

Non-technical entrepreneurs and small companies.

Industry/Entity Type

University

Requirements
Must have
• My company logo.
In any way, both colors from my logo.
First- and last name, e-mail and phone number.
Double-sided design.
Nice to have
• Something creative with the symbol in my logo

```html
<!DOCTYPE html>
<html lang="en">
<head>
<meta charset="utf-8">
<title>Brimlo Software – Business Card</title>
<link rel="stylesheet" href="https://fonts.googleapis.com/css2?family=Arimo:wght@400;700&display=swap">
<style>
  :root {
    --page-bg: #ffffff;
    --brand-blue: #2a7de1;
    --brand-dark: #333333;
    --card-front: #808080;
    --card-back: #3a3a3a;
    --card-back-tone: #2f2f2f;
    --text-dark: #2b2b2b;
  }
  * { box-sizing: border-box; margin: 0; padding: 0; }
  html, body {
    width: 1200px;
    height: 1200px;
    overflow: hidden;
    background: var(--page-bg);
    font-family: "Arimo", Arial, sans-serif;
  }
  .canvas {
    position: relative;
    width: 1200px;
    height: 1200px;
  }

  /* Brand presentation */
  .brand-lockup {
    position: absolute;
    left: 44px;
    top: 640px;
    display: flex;
    align-items: center;
    gap: 34px;
  }
  .brand-lockup .brand-dot {
    width: 150px;
    height: 150px;
    border-radius: 50%;
    background: var(--brand-blue);
  }
  .brand-lockup .brand-name {
    font-size: 112px;
    font-weight: 400;
    color: var(--brand-dark);
    letter-spacing: 2px;
    line-height: 1;
  }

  /* Cards */
  .card {
    position: absolute;
    width: 222px;
    height: 390px;
  }
  .card-back {
    left: 695px;
    top: 405px;
    background: var(--card-back);
  }
  .card-back .pattern {
    position: absolute;
    inset: 0;
    background: linear-gradient(160deg, var(--card-back) 0%, var(--card-back-tone) 100%);
  }
  .card-back .back-mark {
    position: absolute;
    left: 170px;
    top: 312px;
    width: 22px;
    height: 22px;
    border-radius: 50%;
    background: var(--brand-blue);
  }

  .card-front {
    left: 943px;
    top: 409px;
    width: 221px;
    height: 386px;
    background: var(--card-front);
    color: var(--text-dark);
  }
  .card-front .holder-name {
    position: absolute;
    left: 16px;
    top: 20px;
    font-size: 20px;
    font-weight: 700;
    color: var(--brand-blue);
    letter-spacing: 0.3px;
  }
  .card-front .holder-role {
    position: absolute;
    left: 16px;
    top: 42px;
    font-size: 10px;
    font-weight: 700;
    letter-spacing: 0.3px;
  }
  .card-front .divider {
    position: absolute;
    left: 16px;
    top: 66px;
    width: 128px;
    height: 2px;
    background: var(--text-dark);
  }
  .card-front .contact {
    position: absolute;
    left: 16px;
    top: 84px;
    list-style: none;
    font-size: 12px;
    line-height: 18px;
  }
  .card-front .card-brand {
    position: absolute;
    left: 58px;
    top: 318px;
    display: flex;
    align-items: center;
    gap: 8px;
  }
  .card-front .card-brand .brand-dot {
    width: 26px;
    height: 26px;
    border-radius: 50%;
    background: var(--brand-blue);
  }
  .card-front .card-brand .brand-name {
    font-size: 26px;
    font-weight: 400;
    color: var(--brand-dark);
    line-height: 1;
  }
</style>
</head>
<body>
<main class="canvas">
  <div class="brand-lockup">
    <span class="brand-dot"></span>
    <span class="brand-name">brimlo</span>
  </div>

  <section class="card card-back">
    <div class="pattern" role="img" aria-label="Repeating pattern of interlocking rounded brand shapes in dark grey"></div>
    <span class="back-mark"></span>
  </section>

  <section class="card card-front">
    <h1 class="holder-name">JOHN DOE</h1>
    <p class="holder-role">FOUNDER</p>
    <div class="divider"></div>
    <ul class="contact">
      <li>888.555.0142</li>
      <li>JOHN@BRIMLO.COM</li>
    </ul>
    <div class="card-brand">
      <span class="brand-dot"></span>
      <span class="brand-name">brimlo</span>
    </div>
  </section>
</main>
</body>
</html>
```